Marketing Flyer

I need a flyer for my marketing company. I would like for it to to be consistent with my logo and business card design. I would also like for there to be an image of a crowded waiting room, or restaurant with people gathered around a flat screen that reads "Your Ad Here".

• logo, info on attached doc.
• Possibly a picture people in a waiting room or restaurant with a digital sign present that reads "your ad here".

```html
<!DOCTYPE html>
<html lang="en">
<head>
<meta charset="utf-8">
<title>FieldLine Marketing – Flyer</title>
<link href="https://fonts.googleapis.com/css2?family=Lato:wght@400;700;900&family=Montserrat:wght@400;700;800&display=swap" rel="stylesheet">
<style>
  :root{
    --green:#5a9e2a;
    --green-light:#6fb432;
    --grey-dark:#4a4a4a;
    --grey-mid:#6d6d6d;
    --grey-text:#555;
    --ink:#2a2a2a;
    --paper:#ffffff;
    --stage:#e8e8e8;
  }
  *{box-sizing:border-box;margin:0;padding:0}
  html,body{width:1200px;height:1200px;overflow:hidden}
  body{background:var(--stage);font-family:"Lato",sans-serif;color:var(--grey-text);position:relative}
  .flyer{position:absolute;left:180px;top:20px;width:840px;height:1160px;background:var(--paper);overflow:hidden;box-shadow:0 4px 18px rgba(0,0,0,.18)}

  .brand{position:absolute;top:26px;left:0;width:100%;display:flex;justify-content:center;align-items:center;gap:12px}
  .brand-mark{width:22px;height:22px;border-radius:50%;background:var(--green)}
  .brand-text{text-align:left}
  .brand-name{font-family:"Montserrat",sans-serif;font-weight:700;font-size:44px;color:var(--grey-dark);line-height:1}
  .brand-sub{font-family:"Montserrat",sans-serif;font-weight:400;font-size:13px;letter-spacing:9px;color:var(--grey-mid);margin-left:30px}

  .scene{position:absolute;top:110px;left:0;width:100%;height:360px;
    background:linear-gradient(180deg,#9a5446 0%,#874638 45%,#5e3a33 75%,#4a4550 100%)}
  .screen{position:absolute;background:#fff;border:6px solid #1c1c1c;display:flex;align-items:center;justify-content:center;
    font-family:"Montserrat",sans-serif;font-weight:800;color:var(--ink);box-shadow:0 3px 8px rgba(0,0,0,.35)}
  .screen em{font-style:normal;color:var(--green-light);margin:0 .25em}
  .screen-main{left:260px;top:40px;width:340px;height:175px;font-size:32px}
  .screen-right{left:630px;top:30px;width:195px;height:100px;font-size:16px}
  .screen-left{left:20px;top:140px;width:210px;height:105px;font-size:17px}

  .headline-band{position:absolute;top:430px;left:0;width:100%;height:140px;background:var(--green);
    clip-path:polygon(0 32%,100% 0,100% 100%,0 100%);color:#fff;text-align:center;padding-top:50px}
  .headline-band .line1{font-family:"Montserrat",sans-serif;font-weight:400;font-size:30px;letter-spacing:1px}
  .headline-band .line2{font-family:"Montserrat",sans-serif;font-weight:800;font-size:34px;letter-spacing:.5px}

  .benefits-tab{position:absolute;top:570px;left:60px;width:720px;height:58px;border-radius:0 0 30px 30px;
    background:linear-gradient(180deg,#5f5f5f,#3f3f3f);color:#fff;display:flex;align-items:center;justify-content:center;
    font-family:"Montserrat",sans-serif;font-size:21px;letter-spacing:3px}

  .benefit{position:absolute;display:flex;align-items:flex-start;gap:10px;width:395px}
  .benefit-icon{flex:none;width:42px;height:42px;border-radius:50%;border:2px solid #d5d5d5;background:#fff;display:flex;align-items:center;justify-content:center}
  .benefit-icon svg{width:24px;height:24px}
  .benefit-body{display:flex;gap:10px;align-items:flex-start}
  .benefit-label{flex:none;background:var(--green);color:#fff;font-family:"Lato",sans-serif;font-weight:900;font-size:14px;
    padding:4px 14px;border-radius:0 14px 14px 0;margin-top:9px;min-width:120px}
  .benefit-text{font-size:13px;line-height:1.35;color:var(--grey-text);padding-top:2px}

  .price{position:absolute;top:918px;left:180px;width:560px;height:64px;border:2px solid #777;border-radius:34px;
    display:flex;align-items:center;justify-content:center;gap:12px}
  .price-lead{font-family:"Lato",sans-serif;font-size:24px;letter-spacing:1px;color:var(--grey-dark)}
  .price-amount{font-family:"Montserrat",sans-serif;font-weight:800;font-size:38px;color:var(--green)}
  .price-per{background:var(--green);color:#fff;font-size:11px;font-weight:700;line-height:1.1;padding:3px 6px;letter-spacing:1px}

  .what-we-do{position:absolute;top:1000px;left:0;width:100%;height:46px;display:flex}
  .what-label{width:230px;background:var(--green);color:#fff;font-family:"Montserrat",sans-serif;font-weight:700;font-size:20px;
    display:flex;align-items:center;justify-content:center}
  .what-text{flex:1;background:var(--grey-dark);color:#fff;font-size:16px;display:flex;align-items:center;padding-left:22px}

  .contact{position:absolute;top:1066px;left:0;width:100%;height:80px;display:flex;align-items:center;padding:0 40px;gap:18px}
  .call-label{font-family:"Montserrat",sans-serif;font-size:28px;color:var(--grey-dark);letter-spacing:1px}
  .call-number{background:var(--green);color:#fff;font-family:"Montserrat",sans-serif;font-weight:700;font-size:28px;padding:8px 26px;border-radius:30px}
  .contact-lines{margin-left:auto;display:flex;flex-direction:column;gap:8px}
  .contact-line{display:flex;align-items:center;gap:8px;font-size:15px;font-weight:700;color:var(--grey-dark)}
  .contact-dot{width:22px;height:22px;border-radius:50%;background:var(--green);display:flex;align-items:center;justify-content:center}
  .contact-dot svg{width:12px;height:12px}
</style>
</head>
<body>
<main class="flyer">

  <header class="brand">
    <span class="brand-mark"></span>
    <div class="brand-text">
      <div class="brand-name">FieldLine</div>
      <div class="brand-sub">MARKETING</div>
    </div>
  </header>

  <section class="scene" role="img" aria-label="Photo of a restaurant with a brick wall where guests sit watching wall-mounted screens">
    <div class="screen screen-left">Your<em>Ad</em>Here</div>
    <div class="screen screen-main">Your<em>Ad</em>Here</div>
    <div class="screen screen-right">Your<em>Ad</em>Here</div>
  </section>

  <section class="headline-band">
    <div class="line1">LET US MAKE YOU</div>
    <div class="line2">FAMOUS IN YOUR COMMUNITY!</div>
  </section>

  <div class="benefits-tab">BENEFITS OF ADVERTISING WITH FIELDLINE</div>

  <div class="benefit" style="left:28px;top:648px">
    <div class="benefit-icon"><svg viewBox="0 0 24 24"><polygon points="12,2 15,9 22,9 16.5,13.5 18.5,21 12,16.5 5.5,21 7.5,13.5 2,9 9,9" fill="var(--green)"/></svg></div>
    <div class="benefit-body"><span class="benefit-label">Exclusivity</span><span class="benefit-text">Only 2 ads per industry.</span></div>
  </div>
  <div class="benefit" style="left:28px;top:702px">
    <div class="benefit-icon"><svg viewBox="0 0 24 24"><rect x="3" y="3" width="18" height="18" rx="2" fill="none" stroke="var(--green)" stroke-width="2.5"/><path d="M7 17 L17 7 M11 7 H17 V13" fill="none" stroke="var(--green)" stroke-width="2.5"/></svg></div>
    <div class="benefit-body"><span class="benefit-label">Exposure</span><span class="benefit-text">Our digital signage is placed in only the best/high traffic businesses in your area.</span></div>
  </div>
  <div class="benefit" style="left:28px;top:768px">
    <div class="benefit-icon"><svg viewBox="0 0 24 24"><path d="M4 10 H18 L14 6 M20 14 H6 L10 18" fill="none" stroke="var(--green)" stroke-width="2.5"/></svg></div>
    <div class="benefit-body"><span class="benefit-label">Repetition</span><span class="benefit-text">Your ad is shown over 3,500 time each month (42,000 times per year)!</span></div>
  </div>
  <div class="benefit" style="left:28px;top:824px">
    <div class="benefit-icon"><svg viewBox="0 0 24 24"><circle cx="6" cy="8" r="3" fill="var(--green)"/><circle cx="12" cy="6" r="3" fill="var(--green)"/><circle cx="18" cy="8" r="3" fill="var(--green)"/><rect x="3" y="12" width="18" height="8" rx="3" fill="var(--green)"/></svg></div>
    <div class="benefit-body"><span class="benefit-label">Local</span><span class="benefit-text">We show your ad to consumers in YOUR area. Let us help you do business with the people you want to do business with.</span></div>
  </div>

  <div class="benefit" style="left:430px;top:648px">
    <div class="benefit-icon"><svg viewBox="0 0 24 24"><path d="M5 4 V12 A7 7 0 0 0 19 12 V4 H15 V12 A3 3 0 0 1 9 12 V4 Z" fill="var(--green)"/></svg></div>
    <div class="benefit-body"><span class="benefit-label">Lead Generation</span><span class="benefit-text">We show consumers how to reach you and where to find you.</span></div>
  </div>
  <div class="benefit" style="left:430px;top:712px">
    <div class="benefit-icon"><svg viewBox="0 0 24 24"><path d="M3 10 L12 4 L21 10 Z" fill="var(--green)"/><rect x="5" y="11" width="14" height="9" fill="var(--green)"/></svg></div>
    <div class="benefit-body"><span class="benefit-label">Brand Awareness</span><span class="benefit-text">People need to know your business. We make that happen by putting your brand right in front of them.</span></div>
  </div>
  <div class="benefit" style="left:430px;top:800px">
    <div class="benefit-icon"><svg viewBox="0 0 24 24"><rect x="3" y="5" width="18" height="12" rx="1.5" fill="none" stroke="var(--green)" stroke-width="2.5"/><path d="M9 20 H15" stroke="var(--green)" stroke-width="2.5"/></svg></div>
    <div class="benefit-body"><span class="benefit-label">Digital</span><span class="benefit-text">Digital advertising has higher retention rates and higher consumer engagement.</span></div>
  </div>

  <div class="price">
    <span class="price-lead">Inexpensive Only</span>
    <span class="price-amount">$31.00</span>
    <span class="price-per">PER<br>MONTH!</span>
  </div>

  <section class="what-we-do">
    <div class="what-label">WHAT WE DO:</div>
    <div class="what-text">We design an ad for your company and place it on the TV at local businesses.</div>
  </section>

  <footer class="contact">
    <span class="call-label">CALL US NOW</span>
    <span class="call-number">+111111111</span>
    <div class="contact-lines">
      <div class="contact-line"><span class="contact-dot"><svg viewBox="0 0 12 12"><rect x="1" y="2.5" width="10" height="7" fill="none" stroke="#fff" stroke-width="1.4"/><path d="M1 3 L6 7 L11 3" fill="none" stroke="#fff" stroke-width="1.4"/></svg></span>hello@fieldline-ads.com</div>
      <div class="contact-line"><span class="contact-dot"><svg viewBox="0 0 12 12"><circle cx="6" cy="6" r="4.5" fill="none" stroke="#fff" stroke-width="1.4"/><path d="M1.5 6 H10.5 M6 1.5 V10.5" stroke="#fff" stroke-width="1.2"/></svg></span>www.fieldline-ads.com</div>
    </div>
  </footer>

</main>
</body>
</html>
```